YouTube video thumbnail for my simple healthy recipes channel

Hi,

I need a thumbnail that I can re-use for all my videos and only substitute the photo of the recipe/food and maybe the name of the food/recipe if you will include that.

The goal is to attract young people (especially women) that are interested in simple healthy recipes. Please try to use light colors and preferably a shade of #a8d9de and or #debc63 to match my upcoming website.

Here is a Google Drive folder with some materials (photos etc.) to use. There is also a design of my new website so you can match the style.

https://filebox.examplestore.net/shared/7Qx2LmVpR8sTzKw3NbHd5yEa91?view=open

Here is my channel: https://www.vidplaza.example.org/c/VPmRt8ZqWnE2bLsHx7Yd4kGf

Thank you,
+Marta

Target Market(s)

Young Women

Industry/Entity Type

Nutritionist

Font styles to use
Other font styles liked:
• Lato preferred but you can be creative

Colors
ffffff

Requirements
Must have
• as above
Nice to have
• as above
Should not have
• as above

```html
<!DOCTYPE html>
<html lang="en">
<head>
<meta charset="utf-8">
<title>Marta Veldan – Channel</title>
<link rel="stylesheet" href="https://fonts.googleapis.com/css2?family=Roboto:wght@400;500&family=Lato:wght@400;700&family=Allura&display=swap">
<style>
  :root {
    --page-bg: #f1f1f1;
    --card-bg: #ffffff;
    --border: #e3e3e3;
    --text-dark: #222222;
    --text-muted: #767676;
    --link-blue: #1f6fc5;
    --subscribe-red: #e62117;
    --band-gold: #d7b45c;
    --script-ink: #111111;
    --search-btn: #f8f8f8;
  }
  * { margin: 0; padding: 0; box-sizing: border-box; }
  html, body { width: 1200px; height: 534px; overflow: hidden; }
  body {
    position: relative;
    background: var(--page-bg);
    font-family: "Roboto", Arial, sans-serif;
    color: var(--text-dark);
  }
  .top-bar {
    position: absolute; left: 0; top: 0; width: 1200px; height: 44px;
    background: var(--card-bg);
    border-bottom: 1px solid var(--border);
  }
  .search-field {
    position: absolute; left: 0; top: 9px; width: 400px; height: 25px;
    border: 1px solid #cccccc; border-left: none; background: #fff;
  }
  .search-button {
    position: absolute; left: 400px; top: 9px; width: 59px; height: 25px;
    border: 1px solid #d3d3d3; background: var(--search-btn);
  }
  .search-button svg { position: absolute; left: 23px; top: 5px; }

  .channel-card {
    position: absolute; left: 45px; top: 44px; width: 1120px; height: 258px;
    background: var(--card-bg);
    box-shadow: 0 1px 2px rgba(0,0,0,.1);
  }
  .channel-banner {
    position: absolute; left: 0; top: 0; width: 1120px; height: 185px;
    background: linear-gradient(90deg,
      #d8324a 0%, #c9243a 12%, #e0331f 22%, #f28a1c 33%,
      #f7cf1e 43%, #9fd14a 53%, #6cb23a 63%, #3f8f2c 73%,
      #3a3b6e 84%, #7a2c4a 100%);
    overflow: hidden;
  }
  .banner-title {
    position: absolute; left: 280px; top: 8px;
    font-family: "Allura", cursive;
    font-size: 132px; line-height: 1;
    color: var(--script-ink);
    white-space: nowrap;
  }
  .channel-avatar {
    position: absolute; left: 13px; top: 0; width: 88px; height: 89px;
    background: linear-gradient(160deg, #e8c7a8 0%, #c98a5a 55%, #a7dbe0 100%);
  }
  .channel-name {
    position: absolute; left: 13px; top: 242px; transform: translateY(-100%);
    font-size: 16px; font-weight: 500; color: var(--text-dark);
  }
  .channel-name { top: 220px; transform: none; }
  .subscribe {
    position: absolute; left: 1004px; top: 211px; display: flex; height: 20px;
    font-size: 11px;
  }
  .subscribe-button {
    display: flex; align-items: center; gap: 5px;
    background: var(--subscribe-red); color: #fff; font-weight: 500;
    padding: 0 6px; height: 20px;
  }
  .subscribe-mark { width: 9px; height: 9px; background: #fff; }
  .subscriber-count {
    display: flex; align-items: center; padding: 0 6px;
    border: 1px solid #ccc; border-left: none; color: #555; background: #fafafa;
  }

  .uploads-card {
    position: absolute; left: 45px; top: 310px; width: 1120px; height: 196px;
    background: var(--card-bg);
    box-shadow: 0 1px 2px rgba(0,0,0,.1);
  }
  .uploads-heading {
    position: absolute; left: 16px; top: 16px;
    font-size: 14px; font-weight: 500;
  }
  .video { position: absolute; top: 40px; }
  .video:nth-of-type(1) { left: 15px; width: 176px; }
  .video:nth-of-type(2) { left: 201px; width: 172px; }
  .video:nth-of-type(3) { left: 382px; width: 171px; }
  .thumbnail {
    position: relative; height: 98px; overflow: hidden;
  }
  .thumbnail-photo { position: absolute; inset: 0; }
  .photo-salmon { background: linear-gradient(120deg, #e9e9ec 0%, #c58a55 45%, #9a5e34 100%); }
  .photo-salad { background: radial-gradient(ellipse at 55% 40%, #7fbf4a 0%, #3f7d2a 45%, #2a3a3a 100%); }
  .photo-potatoes { background: radial-gradient(ellipse at 65% 45%, #d9b35a 0%, #8a6a3a 50%, #efefef 100%); }
  .thumbnail-band {
    position: absolute; left: 0; top: 28px; width: 100%; height: 37px;
    background: var(--band-gold); opacity: .92;
    display: flex; flex-direction: column; justify-content: center;
    padding-left: 7px;
    font-family: "Lato", sans-serif; font-weight: 700; color: #fff;
    font-size: 11.5px; line-height: 1.1; text-transform: uppercase;
  }
  .thumbnail-band .band-kicker { font-size: 6px; letter-spacing: .5px; }
  .thumbnail-signature {
    position: absolute; left: 8px; top: 70px;
    font-family: "Allura", cursive; font-size: 19px; color: var(--script-ink);
  }
  .video-title {
    margin-top: 4px; font-size: 11.5px; line-height: 14px;
    color: var(--link-blue); font-weight: 500;
    overflow: hidden; white-space: normal; height: 28px;
  }
  .video-meta { margin-top: 1px; font-size: 10px; color: var(--text-muted); }
</style>
</head>
<body>
  <header class="top-bar">
    <div class="search-field"></div>
    <div class="search-button">
      <svg width="13" height="13" viewBox="0 0 13 13" aria-hidden="true">
        <circle cx="5" cy="5" r="4" fill="none" stroke="#777" stroke-width="1.6"/>
        <line x1="8" y1="8" x2="12" y2="12" stroke="#777" stroke-width="1.8"/>
      </svg>
    </div>
  </header>

  <section class="channel-card">
    <div class="channel-banner" role="img" aria-label="Diagonal strips of fresh produce: raspberries, tomato, orange, corn, lettuce, kiwi, broccoli, plums and grapes">
      <div class="banner-title">Marta Veldan</div>
    </div>
    <div class="channel-avatar" role="img" aria-label="Channel profile photo"></div>
    <h1 class="channel-name">Marta Veldan</h1>
    <div class="subscribe">
      <span class="subscribe-button"><span class="subscribe-mark"></span>Subscribe</span>
      <span class="subscriber-count">26</span>
    </div>
  </section>

  <section class="uploads-card">
    <h2 class="uploads-heading">Uploads</h2>

    <article class="video">
      <div class="thumbnail">
        <div class="thumbnail-photo photo-salmon" role="img" aria-label="Photo of salmon patties on a plate"></div>
        <div class="thumbnail-band"><span>Vegetable packed</span><span>salmon patties</span></div>
        <div class="thumbnail-signature">Marta Veldan</div>
      </div>
      <p class="video-title">Vegetable Packed Salmon Patties | Simple Healthy Recipe...</p>
      <p class="video-meta">2,101 views • 7 hours ago</p>
    </article>

    <article class="video">
      <div class="thumbnail">
        <div class="thumbnail-photo photo-salad" role="img" aria-label="Photo of a fresh green salad in a bowl"></div>
        <div class="thumbnail-band"><span class="band-kicker">5 minute</span><span>Fresh salad</span></div>
        <div class="thumbnail-signature">Marta Veldan</div>
      </div>
      <p class="video-title">5 Minute Fresh Salad | Simple Healthy Recipes | Marta Veldan</p>
      <p class="video-meta">10,339 views • 4 days ago</p>
    </article>

    <article class="video">
      <div class="thumbnail">
        <div class="thumbnail-photo photo-potatoes" role="img" aria-label="Photo of baked potatoes with mushrooms and herbs"></div>
        <div class="thumbnail-band"><span>Baked potatoes</span><span>with mushrooms</span></div>
        <div class="thumbnail-signature">Marta Veldan</div>
      </div>
      <p class="video-title">Tasty Baked Potatoes with Mushrooms | Simple Healthy...</p>
      <p class="video-meta">14,623 views • 1 week ago</p>
    </article>
  </section>
</body>
</html>
```